A5 Flyer for Window Cleaning Company

2 sided Flyer design required for window cleaning company. One side to include we use traditional and hot water fed pole window cleaning systems, conservatory cleaning, and fascia and soffit cleaning. The other side to be for Gutter cleaning. See the must haves section of project brief for more info. Mixture of some images and text for both sides. ( do not have to use all images supplied). The flyer will be used to promote the business to new residential customers.

Target Market(s)

Private households/new customers

Industry/Entity Type

Window Cleaning

Font styles to use
Serif

Requirements
Must have
• Company address ( 7 Old Pennick Court Harlow Street Edinburgh EH4 9RQ
Phone numbers( 0131 482 7719 0800 061 2287).
Website and email address ( info@falconbright-cleaning.example)
Excellent Customer Service. Competitive prices. Established 1994.
Side 1of flyer = Falconbright Window Cleaning Side 2 of flyer Falconbright Gutter Cleaning.
Nice to have
• Professional look.

```html
<!DOCTYPE html>
<html lang="en">
<head>
<meta charset="utf-8">
<title>Falconbright Window Cleaning – A5 Flyer</title>
<link rel="stylesheet" href="https://fonts.googleapis.com/css2?family=Noto+Serif+Display:wdth,wght@62.5..100,700..900&family=Noto+Serif:wght@400;700&family=Noto+Sans:wght@400;500&display=swap">
<style>
  :root{
    --page:#ffffff;
    --ink:#111111;
    --white:#ffffff;
    --panel-box:#2a86a8;
    --logo-tile:#6fa8dc;
    --front-top:#35186c;
    --front-mid:#2c5aa6;
    --front-teal:#2a90b1;
    --front-bottom:#063a78;
    --back-top:#c42a9f;
    --back-mid:#6c1fd3;
    --back-bottom:#3b2aa6;
    --display:"Noto Serif Display", Georgia, serif;
    --serif:"Noto Serif", Georgia, serif;
    --sans:"Noto Sans", Arial, sans-serif;
  }
  *{box-sizing:border-box;margin:0;padding:0}
  html,body{width:1200px;height:844px;overflow:hidden;background:var(--page)}
  .canvas{position:relative;width:1200px;height:844px}
  .side-label{position:absolute;top:14px;width:537px;text-align:center;font-family:var(--serif);font-size:17px;color:var(--ink)}
  .flyer{position:absolute;top:42px;width:537px;height:758px;overflow:hidden;color:var(--white)}
  .flyer--front{left:40px;background:linear-gradient(180deg,var(--front-top) 0%,var(--front-mid) 40%,var(--front-teal) 68%,var(--front-bottom) 100%)}
  .flyer--back{left:623px;background:linear-gradient(180deg,var(--back-top) 0%,var(--back-mid) 45%,var(--back-mid) 70%,var(--back-bottom) 100%)}

  .brand{position:absolute;left:18px;top:18px;width:70px;display:flex;flex-direction:column;align-items:center;gap:4px;z-index:3}
  .brand__mark{width:30px;height:30px;background:var(--logo-tile)}
  .brand__name{font-family:var(--serif);font-weight:700;font-size:10px;line-height:1.15;text-align:center;color:var(--white)}

  .hero-photo{position:absolute;left:28px;top:20px;width:500px;height:340px;border-radius:40px 60px 30px 50px;
    background:radial-gradient(ellipse at 55% 40%,#e4ecf2 0%,#9fb4c4 35%,#4f7a5c 70%,rgba(70,90,150,0) 100%)}
  .thumb-circle{position:absolute;top:293px;width:124px;height:124px;border-radius:50%;border:2px solid var(--white);z-index:2}
  .thumb-circle--1{left:40px;background:linear-gradient(160deg,#a9bfe0,#5f7fae)}
  .thumb-circle--2{left:206px;background:linear-gradient(160deg,#e9eef2,#8d9aa6)}
  .thumb-circle--3{left:369px;background:linear-gradient(160deg,#c8d2dc,#6b5d66)}

  .headline{position:absolute;left:0;width:537px;overflow:visible}
  .headline text{font-family:var(--display);font-stretch:62.5%;font-weight:800;fill:var(--white)}

  .info-box{position:absolute;background:var(--panel-box);border-radius:12px}
  .info-box--front{left:31px;top:625px;width:479px;height:95px;padding:14px 15px 0}
  .info-box__title{font-family:var(--serif);font-weight:700;font-size:15.5px;letter-spacing:.3px;line-height:1.1}
  .info-box__body{font-family:var(--sans);font-size:12.3px;line-height:15.2px;text-align:justify;text-align-last:left;margin-top:1px}

  .gutter-photo{position:absolute;left:0;top:0;width:537px;height:275px;
    background:linear-gradient(180deg,rgba(196,42,159,.25) 0%,rgba(0,0,0,0) 20%),
      radial-gradient(ellipse at 62% 35%,#c98a2e 0%,#8c6a4a 30%,#b9b3bc 55%,rgba(140,60,200,0) 100%),
      linear-gradient(180deg,#8a8a90 0%,#d8d4dc 50%,#7a3fc0 100%)}
  .thumb-rect{position:absolute;top:272px;height:101px;border:2px solid var(--white)}
  .thumb-rect--1{left:29px;width:155px;background:linear-gradient(90deg,#7fa6d6 0%,#9a5a44 45%,#e6e9ee 100%)}
  .thumb-rect--2{left:191px;width:155px;background:linear-gradient(180deg,#f1f1f3,#9ea7b2)}
  .thumb-rect--3{left:353px;width:155px;background:linear-gradient(120deg,#8fa0ae,#c9d3da 55%,#7c3b46)}

  .info-box--back{left:32px;top:528px;width:473px;height:134px;padding:9px 18px 0}
  .service-intro,.service-list{font-family:var(--sans);font-size:12px;line-height:14.4px;letter-spacing:.2px}
  .service-list{list-style:none}
  .service-list li::before{content:"\2022";margin-right:5px}

  .contact{position:absolute;left:0;width:537px;text-align:center;font-family:var(--serif)}
  .contact__address{top:676px;font-size:12px;letter-spacing:1.1px;display:flex;justify-content:center;align-items:center;gap:6px}
  .contact__phones{top:695px;font-size:30px;line-height:36px;display:flex;justify-content:center;align-items:center;gap:6px}
  .contact__online{top:733px;font-size:12px;display:flex;justify-content:center;align-items:center;gap:6px}
  .contact__online span{display:inline-flex;align-items:center;gap:4px}
  .icon{fill:var(--white)}
</style>
</head>
<body>
<div class="canvas">
  <div class="side-label" style="left:40px">A5 Flyer_Front</div>
  <div class="side-label" style="left:623px">A5 Flyer_Back</div>

  <section class="flyer flyer--front">
    <div class="brand"><div class="brand__mark"></div><div class="brand__name">Falconbright Window Cleaning</div></div>
    <div class="hero-photo" role="img" aria-label="Window cleaner in a blue cap washing a large window with a scrubber in a sunny garden"></div>
    <div class="thumb-circle thumb-circle--1" role="img" aria-label="Water fed pole brush spraying water on glass"></div>
    <div class="thumb-circle thumb-circle--2" role="img" aria-label="Red pole brush cleaning a white window frame"></div>
    <div class="thumb-circle thumb-circle--3" role="img" aria-label="Cleaner using a squeegee on an office window"></div>

    <svg class="headline" style="top:450px" width="537" height="180" viewBox="0 0 537 180" aria-label="Exterior window cleaning">
      <text x="46" y="53" font-size="60" textLength="447" lengthAdjust="spacingAndGlyphs">EXTERIOR WINDOW</text>
      <text x="46" y="136" font-size="118" textLength="447" lengthAdjust="spacingAndGlyphs">CLEANING</text>
    </svg>

    <div class="info-box info-box--front">
      <h2 class="info-box__title">NEW WATER FED POLE SYSTEM !</h2>
      <p class="info-box__body">You may have noticed your rames and sills being cleaned by our staff recently. We've done this free of charge as part of our preparation to get your windows ready for our new Water Fed Pole system.</p>
    </div>
  </section>

  <section class="flyer flyer--back">
    <div class="gutter-photo" role="img" aria-label="Gloved hand lifting autumn leaves out of a roof gutter"></div>
    <div class="brand"><div class="brand__mark"></div><div class="brand__name">Falconbright Window Cleaning</div></div>
    <div class="thumb-rect thumb-rect--1" role="img" aria-label="Water fed pole cleaning windows of a brick house"></div>
    <div class="thumb-rect thumb-rect--2" role="img" aria-label="Pole brush cleaning a white conservatory frame"></div>
    <div class="thumb-rect thumb-rect--3" role="img" aria-label="Cleaner working on a glass frontage"></div>

    <svg class="headline" style="top:376px" width="537" height="150" viewBox="0 0 537 150" aria-label="Gutter and rhone cleaning">
      <text x="29" y="48" font-size="56" textLength="476" lengthAdjust="spacingAndGlyphs">GUTTER AND RHONE</text>
      <text x="29" y="137" font-size="108" textLength="474" lengthAdjust="spacingAndGlyphs">CLEANING</text>
    </svg>

    <div class="info-box info-box--back">
      <p class="service-intro">With our new Water Fed Pole system we can offer you even more services and benefits to those listed below:-</p>
      <ul class="service-list">
        <li>Exterior window cleaning&nbsp; Gutter cleaning</li>
        <li>Gutter and rhone cleaning</li>
        <li>Fascia and Soffit cleaning</li>
        <li>Conservatory cleaning</li>
        <li>One-off Cleans</li>
        <li>Builders Cleans</li>
      </ul>
    </div>

    <div class="contact contact__address">
      <svg class="icon" width="9" height="12" viewBox="0 0 9 12" aria-hidden="true"><path d="M4.5 0A4.5 4.5 0 0 0 0 4.5C0 8 4.5 12 4.5 12S9 8 9 4.5A4.5 4.5 0 0 0 4.5 0Zm0 6.3a1.8 1.8 0 1 1 0-3.6 1.8 1.8 0 0 1 0 3.6Z"/></svg>
      7 Old Pennick Court, Harlow Street, Edinburgh EH4 9RQ
    </div>
    <div class="contact contact__phones">
      <svg class="icon" width="8" height="18" viewBox="0 0 8 18" aria-hidden="true"><path d="M6 0 2 1C0 5 0 13 2 17l4 1 1-5-3-1C3 10 3 8 4 6l3-1Z"/></svg>
      0131 482 7719 | 0800 061 2287
    </div>
    <div class="contact contact__online">
      <span><svg class="icon" width="16" height="10" viewBox="0 0 16 10" aria-hidden="true"><path d="M0 0h16v10H0Zm1.5 1 6.5 5 6.5-5Z"/></svg>info@falconbright-cleaning.example</span>
      <span style="margin-left:14px"><svg width="12" height="12" viewBox="0 0 12 12" aria-hidden="true" fill="none" stroke="#fff" stroke-width="1"><circle cx="6" cy="6" r="5.3"/><ellipse cx="6" cy="6" rx="2.4" ry="5.3"/><path d="M.7 6h10.6M1.6 3.3h8.8M1.6 8.7h8.8"/></svg>www.falconbright-cleaning.example</span>
    </div>
  </section>
</div>
</body>
</html>
```